Banner- Clear Out Your Frame (playful)

Looking for a banner design for a course called "Clear Out Your Frame" "with Marla Quist"

Imagine your body like a house made up hundreds of little rooms that creatures can move into (think parasites). The more this stuff moves in, the less room there is for you to be healthy and vibrant. This program teaches people how to evict the squatters/trespassers and powerfully reclaim their body back again.

Looking for more of a light playful concept (both in color and feel) that has fun with the topic.

Dimensions: 900w x 370h
Fonts: (use free fonts) that are bold and strong
colors: any
background: photo, gradient or color (no white or black)
Final product: source, layered psd

Target Market(s)

40-60yro, mature, strong females

Industry/Entity Type

House

Requirements
Must have
• image(s) that communicates the program's theme
Nice to have
• I attached some images of conceptual elements for the design... I'm not attached to these images, just ideas
Should not have
• dark, scary, evil looking things

```html
<!DOCTYPE html>
<html lang="en">
<head>
<meta charset="utf-8">
<title>Clear Out Your Frame — Banner</title>
<link href="https://fonts.googleapis.com/css2?family=Anton&family=Black+Ops+One&display=swap" rel="stylesheet">
<style>
  :root {
    --sun-yellow: #ffc21a;
    --sun-orange: #f26a12;
    --deep-blue: #1c2f7a;
    --night-indigo: #2a1a5c;
    --royal-purple: #5b2a8c;
    --hot-pink: #f0197a;
    --magenta: #c8117a;
    --title-white: #ffffff;
    --title-red: #c4101e;
    --stamp-red: #e0141e;
    --critter-purple: #b57ad6;
    --critter-orange: #c8642a;
  }

  * { margin: 0; padding: 0; box-sizing: border-box; }

  html, body {
    width: 1200px;
    height: 493px;
    overflow: hidden;
    background: var(--night-indigo);
  }

  .banner {
    position: relative;
    width: 1200px;
    height: 493px;
    overflow: hidden;
  }

  .banner__backdrop {
    position: absolute;
    inset: 0;
    background:
      radial-gradient(ellipse 420px 320px at 60px 160px, var(--sun-yellow) 0%, rgba(255,194,26,0.6) 35%, rgba(242,106,18,0) 75%),
      radial-gradient(ellipse 520px 380px at 1150px 260px, var(--hot-pink) 0%, rgba(240,25,122,0.65) 40%, rgba(200,17,122,0) 80%),
      radial-gradient(ellipse 380px 260px at 560px 430px, rgba(91,42,140,0.9) 0%, rgba(91,42,140,0) 80%),
      linear-gradient(100deg, var(--sun-orange) 0%, #c8402a 18%, var(--deep-blue) 40%, var(--night-indigo) 60%, var(--royal-purple) 75%, var(--magenta) 100%);
  }

  .banner__title {
    position: absolute;
    left: 0;
    right: 0;
    top: 56px;
    text-align: center;
    font-family: "Anton", "Arial Narrow", sans-serif;
    font-size: 86px;
    line-height: 1;
    letter-spacing: 1px;
    color: var(--title-white);
    transform: skewX(-10deg);
    -webkit-text-stroke: 2px var(--title-red);
    paint-order: stroke fill;
    text-shadow: 3px 4px 0 var(--title-red), 6px 8px 10px rgba(0,0,0,0.35);
  }

  .banner__host {
    position: absolute;
    left: 692px;
    top: 196px;
    font-family: "Anton", "Arial Narrow", sans-serif;
    font-size: 40px;
    line-height: 1;
    color: var(--title-white);
    transform: skewX(-10deg);
    text-shadow: 2px 3px 0 var(--title-red), 4px 5px 8px rgba(0,0,0,0.3);
  }

  .stamp {
    position: absolute;
    left: 14px;
    top: 282px;
    width: 370px;
    transform: rotate(-4deg);
    font-family: "Black Ops One", "Impact", sans-serif;
    color: var(--stamp-red);
    line-height: 1.05;
    text-align: center;
    -webkit-text-stroke: 6px var(--title-white);
    paint-order: stroke fill;
  }

  .stamp__line { display: block; }
  .stamp__line--top { font-size: 62px; letter-spacing: 1px; }
  .stamp__line--bottom { font-size: 64px; letter-spacing: 2px; margin-left: -40px; }

  .critter {
    position: absolute;
  }

  .critter--runner {
    left: 400px;
    top: 273px;
    width: 160px;
    height: 210px;
    border-radius: 80px 80px 40px 40px;
    background: linear-gradient(160deg, #d3a2ec 0%, var(--critter-purple) 55%, #8a4cb0 100%);
    border: 4px solid var(--title-white);
  }

  .critter--squatter {
    left: 570px;
    top: 300px;
    width: 160px;
    height: 185px;
    border-radius: 70px 70px 50px 50px;
    background: linear-gradient(160deg, #e8904a 0%, var(--critter-orange) 55%, #8f3f1a 100%);
    border: 4px solid var(--title-white);
  }
</style>
</head>
<body>
  <main class="banner">
    <div class="banner__backdrop" role="img" aria-label="Bright angular background shading from sunny yellow and orange on the left through deep blue and indigo to hot pink on the right"></div>

    <h1 class="banner__title">"Clear Out Your Frame"</h1>
    <p class="banner__host">with Marla Quist</p>

    <p class="stamp">
      <span class="stamp__line stamp__line--top">EVICTION</span>
      <span class="stamp__line stamp__line--bottom">ORDER</span>
    </p>

    <div class="critter critter--runner" role="img" aria-label="Cartoon purple creature running away in a hurry"></div>
    <div class="critter critter--squatter" role="img" aria-label="Cartoon orange spotted toad-like creature sitting grumpily"></div>
  </main>
</body>
</html>
```